R&T Night club Presents :

I need a advertiser 4 nights in one poster, from Thursday to Sunday,
Thursday : Every Thursday Irish Night
Friday: Old School Hip Hop, top 40 & request
Sat: Comet Saturdays July 11, July 25, August 8, August 22
Brazilian Night Forro: July 18, August 1, August 15 & August 29
Sunday: Velvet Sundaze ( Dj Marlow & Dj Vobo

Target Market(s)

All 4 Nights

Industry/Entity Type

School

Font styles to use
Decorative
Script

Requirements
Must have
• Poster 11x16 and talk about all 4 nights on, see up there description
Nice to have
• A lot of colors
Should not have
• Address: 812 Kelberry Rd Hyannis MA
• 5087162043
• Starting 9:30pm until 1:00Am
• 21+ ID
• Special Drinks $3.99

```html
<!DOCTYPE html>
<html lang="en">
<head>
<meta charset="utf-8">
<title>R&amp;T Night Club – Four Nights</title>
<link href="https://fonts.googleapis.com/css2?family=Righteous&family=Comfortaa:wght@700&display=swap" rel="stylesheet">
<style>
  :root {
    --page: #efefef;
    --ink: #0b0b0b;
    --white: #ffffff;
    --gold: #d99a2b;
    --green: #2f9a3c;
    --green-deep: #1f7a2a;
    --pink: #e0425a;
    --smoke: #d9d9d9;
    --display: "Righteous", "Comfortaa", sans-serif;
    --small: "Comfortaa", sans-serif;
  }
  * { box-sizing: border-box; margin: 0; padding: 0; }
  html, body { width: 1200px; height: 1000px; overflow: hidden; background: var(--page); }
  .poster {
    position: absolute; left: 280px; top: 20px; width: 641px; height: 960px;
    overflow: hidden; color: var(--white); font-family: var(--display);
    background:
      radial-gradient(ellipse 55% 35% at 52% 48%, rgba(255,255,255,.95) 0%, rgba(220,220,220,.6) 35%, rgba(60,60,60,.3) 70%, transparent 100%),
      radial-gradient(ellipse 70% 50% at 60% 60%, #555 0%, #1c1c1c 60%, var(--ink) 100%);
  }
  .art { position: absolute; }
  .art--shamrock-beer {
    left: 22px; top: 110px; width: 300px; height: 330px; border-radius: 48% 52% 40% 60%;
    background: radial-gradient(circle at 55% 50%, #f3e3b0 0%, #e8b94a 25%, var(--green) 50%, var(--green-deep) 80%, transparent 100%);
  }
  .art--hiphop-figure {
    left: 390px; top: 120px; width: 220px; height: 300px; border-radius: 40% 40% 10% 10%;
    background: radial-gradient(ellipse at 50% 40%, #2a2a2a 0%, #111 60%, transparent 100%);
  }
  .art--boombox {
    left: 275px; top: 300px; width: 320px; height: 90px; transform: rotate(22deg);
    background: linear-gradient(180deg, #cfcfcf, #8d8d8d); opacity: .75; border-radius: 8px;
  }
  .art--splash {
    left: 0; top: 580px; width: 280px; height: 270px; border-radius: 50%;
    background: radial-gradient(circle at 60% 40%, rgba(224,66,90,.85) 0%, rgba(224,66,90,.4) 45%, transparent 75%);
  }
  .art--bottle {
    left: 380px; top: 590px; width: 60px; height: 240px; transform: rotate(-35deg);
    background: linear-gradient(180deg, #9bd36a, #3f7d2b 60%, #c98a6a); border-radius: 20px;
  }
  .art--dancers {
    left: 500px; top: 860px; width: 141px; height: 100px;
    background: radial-gradient(circle at 50% 50%, #c8e04a 0%, #3aa84a 55%, transparent 100%);
  }
  .rot { position: absolute; white-space: nowrap; line-height: 1; }
  .kicker { font-family: var(--small); font-size: 13px; }
  .night { font-size: 40px; }
  .thursday-kicker { left: 55px; top: 88px; transform: rotate(-15deg); }
  .thursday { left: 18px; top: 140px; transform: rotate(-15deg); font-size: 42px; }
  .friday-kicker { left: 460px; top: 28px; transform: rotate(15deg); }
  .friday { left: 330px; top: 40px; transform: rotate(15deg); font-size: 40px; text-align: center; line-height: .95; }
  .friday-extra { left: 385px; top: 150px; transform: rotate(-15deg); font-family: var(--small); font-size: 13px; text-align: center; line-height: 1.2; }
  .club-name { position: absolute; left: 0; width: 100%; text-align: center; color: var(--gold); line-height: 1; }
  .club-name--initials { top: 365px; font-size: 108px; }
  .club-name--word { top: 495px; font-size: 86px; }
  .djs { left: 345px; top: 690px; transform: rotate(60deg); font-family: var(--small); font-size: 16px; text-align: center; line-height: 1.2; }
  .sunday-kicker { left: 385px; top: 745px; transform: rotate(-25deg); }
  .sunday { left: 330px; top: 780px; transform: rotate(-25deg); font-size: 36px; line-height: .95; }
  .saturday { left: 20px; top: 745px; transform: rotate(15deg); font-size: 38px; line-height: .95; }
  .saturday-dates { left: 45px; top: 835px; transform: rotate(15deg); font-family: var(--small); font-size: 12px; }
  .forro-band {
    position: absolute; left: 240px; top: 905px; width: 300px; height: 44px;
    background: var(--green); border-radius: 6px 22px 6px 22px; transform: rotate(-3deg);
    text-align: center; padding-top: 4px;
  }
  .forro-band .also { position: absolute; right: 14px; top: -12px; font-family: var(--small); font-size: 10px; }
  .forro-band .title { font-family: var(--small); font-size: 15px; }
  .forro-band .dates { font-family: var(--small); font-size: 10px; }
</style>
</head>
<body>
  <main class="poster">
    <div class="art art--shamrock-beer" role="img" aria-label="Green shamrock with a foaming mug of beer"></div>
    <div class="art art--hiphop-figure" role="img" aria-label="Silhouette of a hip hop artist in a cap with a gold chain"></div>
    <div class="art art--boombox" role="img" aria-label="Silver boombox"></div>
    <div class="art art--splash" role="img" aria-label="Pink liquid splash"></div>
    <div class="art art--bottle" role="img" aria-label="Champagne bottle spraying"></div>
    <div class="art art--dancers" role="img" aria-label="Dancers in colourful green and yellow powder"></div>

    <p class="rot kicker thursday-kicker">Every Thursday</p>
    <h2 class="rot thursday">Irish Night</h2>

    <p class="rot kicker friday-kicker">Every Friday</p>
    <h2 class="rot friday">Old School<br>Hip Hop</h2>
    <p class="rot friday-extra">Top 40<br>&amp;<br>Request</p>

    <h1>
      <span class="club-name club-name--initials">R&amp;T</span>
      <span class="club-name club-name--word">Night Club</span>
    </h1>

    <p class="rot djs">Dj Marlow<br>&amp;<br>Dj Vobo</p>
    <p class="rot kicker sunday-kicker">Every Sunday</p>
    <h2 class="rot sunday">Velvet<br>Sundaze</h2>

    <h2 class="rot saturday">Comet<br>Saturdays</h2>
    <p class="rot saturday-dates">July 11, July 25, August 8, August 22</p>

    <div class="forro-band">
      <span class="also">also</span>
      <p class="title">Brazilian Night Forro</p>
      <p class="dates">on July 18, August 1, August 15 &amp; August 29</p>
    </div>
  </main>
</body>
</html>
```